Website for an interior designer

We need a new website for Clara Beth Holloway whose new business name is Clara Beth Holloway Interiors. She is a residential interior designer with a mix of modern and contemporary tastes. We are in the process of overhauling her website which is +15 years old and not an accurate reflection of her tastes. The uploaded photos are from some of the houses she has done as well as her logo(s). We would need a section for "About Us" that would have a paragraph of text and bullets showing services and a gallery for photos (~12 total, more to come). A contract page would be optional. The client likes the feel/look of this website: https://www.pondrickstudio.example/ but doesn't want to copy it exactly.

Target Market(s)

Upscale home owners

Industry/Entity Type

Interior Design

Coding

Coded - Design and coding required

Number of Pages Required

4 page

Colors

Designer to choose only greyscale colors for use in the design.

Requirements
Must have
• Home page, about us page, gallery page, contact us page.

```html
<!DOCTYPE html>
<html lang="en">
<head>
<meta charset="utf-8">
<title>Clara Beth Holloway Interiors</title>
<link rel="stylesheet" href="https://fonts.googleapis.com/css2?family=Lato:wght@300;400;700&display=swap">
<style>
:root{
  --ink:#2b2b2b;
  --dark:#444544;
  --mid:#6f6f6f;
  --soft:#9a9a9a;
  --line:#cfcfcf;
  --band:#f5f5f5;
  --band-contact:#efefef;
  --white:#ffffff;
  --tone-1:#e4e4e4;
  --tone-2:#c9c9c9;
  --tone-3:#a8a8a8;
  --tone-4:#7e7e7e;
  --tone-5:#5a5a5a;
  --tone-6:#3a3a3a;
}
*{box-sizing:border-box;margin:0;padding:0}
html,body{width:1200px;height:4336px;overflow:hidden}
body{position:relative;background:var(--white);font-family:"Lato",Arial,sans-serif;color:var(--ink)}
.abs{position:absolute}
.photo{position:absolute;display:block}

/* hero */
.hero{left:0;top:0;width:1200px;height:614px;background:linear-gradient(180deg,#777 0%,#5a5a5a 35%,#6e6e6e 60%,#bcbcbc 100%)}
.hero-title{left:0;width:1200px;top:198px;text-align:center;color:var(--white);font-size:42px;font-weight:700;letter-spacing:.5px}
.hero-sub{left:0;width:1200px;top:264px;text-align:center;color:var(--white);font-size:19px;font-weight:400}
.btn{position:absolute;background:var(--dark);color:var(--white);font-size:15px;font-weight:700;display:flex;align-items:center;justify-content:center;text-transform:uppercase;white-space:nowrap}
.hero-btn{left:539px;top:338px;width:121px;height:34px}

/* nav */
.nav{left:151px;top:559px;width:896px;height:113px;background:var(--dark);color:var(--white)}
.brand{position:absolute;left:40px;top:40px;width:190px;text-align:center;font-size:12px;letter-spacing:1.2px;line-height:17px;font-weight:400;color:var(--white);white-space:nowrap}
.brand small{display:block;font-size:8px;letter-spacing:4px}
.nav-link{position:absolute;top:46px;font-size:17px;transform:translateX(-50%);white-space:nowrap}

/* welcome */
.welcome-1{left:177px;top:790px;font-size:27px;font-weight:400}
.welcome-2{left:174px;top:829px;font-size:27px;font-weight:700;color:var(--mid);white-space:nowrap}
.welcome-text{left:177px;top:912px;width:445px;font-size:14px;line-height:19px;color:var(--mid);text-align:justify}
.welcome-btn{left:177px;top:1089px;width:121px;height:35px}

/* sections */
.services-band{left:0;top:1254px;width:1200px;height:623px;background:var(--band)}
.sec-title{left:0;width:1200px;text-align:center;font-size:27px;font-weight:400}
.sec-title b{color:var(--mid);font-weight:700}
.svc-name{position:absolute;text-align:center;font-size:16px;font-weight:700;line-height:22px;text-transform:uppercase}
.svc-sub{position:absolute;text-align:center;font-size:14px;color:var(--mid);line-height:22px;text-transform:uppercase}
.rule{position:absolute;height:2px;width:70px;background:var(--dark)}
.dot{position:absolute;height:2px;width:22px}

/* gallery */
.caption{left:197px;top:2328px;width:145px;height:62px;background:rgba(60,60,60,.85);color:var(--white);padding:8px 16px}
.caption strong{display:block;font-size:14px;text-transform:uppercase}
.caption span{display:block;font-size:11px;line-height:13px;margin-top:4px}
.gallery-btn{left:507px;top:2888px;width:186px;height:37px}

/* contact */
.contact-band{left:0;top:3023px;width:1200px;height:828px;background:var(--band-contact)}
.contact-lead{left:300px;width:600px;top:3124px;text-align:center;font-size:12px;line-height:17px;color:var(--mid)}
.form-card{left:175px;top:3214px;width:850px;height:500px;background:var(--white)}
.field{position:absolute;border:1px solid var(--line);font-size:13px;color:var(--mid);padding:18px 20px}
.send-btn{left:222px;top:3618px;width:147px;height:46px;font-weight:400;text-transform:none}
.contact-line{top:3783px;font-size:19px;white-space:nowrap}

/* footer */
.foot-name{left:0;width:1200px;top:3998px;text-align:center;font-size:19px;letter-spacing:2px}
.foot-sub{left:0;width:1200px;top:4030px;text-align:center;font-size:11px;letter-spacing:5px}
.foot-link{position:absolute;top:4093px;font-size:15px;color:var(--soft);transform:translateX(-50%)}
.foot-rule{left:0;top:4226px;width:1200px;height:1px;background:#ececec}
.copy{left:0;width:1200px;top:4255px;text-align:center;font-size:13px;color:var(--soft)}
</style>
</head>
<body>

<header>
  <div class="photo hero" role="img" aria-label="Monochrome living room with patterned feature wall, lamps, sofas and a black lounge chair"></div>
  <h1 class="abs hero-title">ELEGANT AND INNOVATIVE</h1>
  <p class="abs hero-sub">Clara Beth Holloway has extensive experience in all aspects of interior design</p>
  <a class="btn hero-btn">Read More</a>

  <nav class="abs nav">
    <div class="brand">CLARA BETH HOLLOWAY<small>INTERIORS</small></div>
    <span class="nav-link" style="left:317px">HOME</span>
    <span class="nav-link" style="left:438px">ABOUT US</span>
    <span class="nav-link" style="left:556px">SERVICES</span>
    <span class="nav-link" style="left:675px">GALLERY</span>
    <span class="nav-link" style="left:795px">CONTACT</span>
  </nav>
</header>

<section class="welcome">
  <svg class="abs" style="left:0;top:830px" width="80" height="150" viewBox="0 0 80 150">
    <polygon points="10,11 71,72 10,133 -51,72" fill="none" stroke="#e2e2e2" stroke-width="1.5"/>
  </svg>
  <h2 class="abs welcome-1">WELCOME TO</h2>
  <h2 class="abs welcome-2">CLARA BETH HOLLOWAY INTERIORS</h2>
  <p class="abs welcome-text">Clara Beth Holloway has extensive experience in all aspects of interior design. She has worked on a wide array of residential and commercial projects in her hometown of Houston and across the United States. Clara Beth's taste can best be described as a sophisticated blend of modern and traditional styles that combine to create a clean, timeless space.</p>
  <a class="btn welcome-btn">Read More</a>

  <svg class="abs" style="left:630px;top:760px" width="490" height="460" viewBox="630 760 490 460">
    <defs>
      <linearGradient id="g-sunroom" x1="0" y1="0" x2="1" y2="1"><stop offset="0" stop-color="#9a9a9a"/><stop offset="1" stop-color="#555555"/></linearGradient>
      <linearGradient id="g-dining" x1="0" y1="0" x2="1" y2="1"><stop offset="0" stop-color="#ececec"/><stop offset="1" stop-color="#b0b0b0"/></linearGradient>
      <linearGradient id="g-lounge" x1="0" y1="0" x2="1" y2="1"><stop offset="0" stop-color="#f0f0f0"/><stop offset="1" stop-color="#c4c4c4"/></linearGradient>
    </defs>
    <g role="img" aria-label="Sunroom with wooden doors and a dining area">
      <polygon points="845,768 1012,934 845,1100 678,934" fill="#3a3a3a"/>
      <polygon points="845,782 998,934 845,1086 692,934" fill="url(#g-sunroom)"/>
    </g>
    <g role="img" aria-label="White dining room with tulip table and chairs">
      <polygon points="978,778 1111,910 978,1042 846,910" fill="#8a8a8a"/>
      <polygon points="978,792 1097,910 978,1028 860,910" fill="url(#g-dining)"/>
    </g>
    <g role="img" aria-label="Cream lounge with curved sofa and flowers">
      <polygon points="772,950 905,1082 772,1214 640,1082" fill="#8f8f8f"/>
      <polygon points="772,964 891,1082 772,1200 654,1082" fill="url(#g-lounge)"/>
    </g>
  </svg>
</section>

<section>
  <div class="abs services-band"></div>
  <svg class="abs" style="left:78px;top:1345px" width="200" height="220" viewBox="0 0 200 220">
    <polygon points="82,5 177,100 82,195 -13,100" fill="none" stroke="#e2e2e2" stroke-width="1.5"/>
  </svg>
  <svg class="abs" style="left:1055px;top:1530px" width="145" height="270" viewBox="0 0 145 270">
    <polygon points="132,5 262,135 132,265 2,135" fill="none" stroke="#e2e2e2" stroke-width="1.5"/>
  </svg>
  <h2 class="abs sec-title" style="top:1308px">OUR <b>SERVICES</b></h2>

  <div class="photo" style="left:175px;top:1397px;width:261px;height:259px;background:linear-gradient(180deg,var(--tone-1),var(--tone-2))" role="img" aria-label="Bright living room with patterned rug and glass coffee table"></div>
  <div class="photo" style="left:468px;top:1397px;width:262px;height:259px;background:linear-gradient(180deg,var(--tone-2),var(--tone-4) 50%,var(--tone-2))" role="img" aria-label="Living room with black cabinetry and modern fireplace"></div>
  <div class="photo" style="left:762px;top:1397px;width:263px;height:259px;background:linear-gradient(180deg,var(--tone-5) 0%,var(--tone-5) 60%,var(--tone-4) 61%,var(--tone-3) 100%)" role="img" aria-label="Painted feature wall with framed artwork above a wooden sideboard"></div>

  <div class="svc-name" style="left:175px;top:1686px;width:261px">Concept Origination</div>
  <div class="svc-sub" style="left:175px;top:1709px;width:261px">and Project Management</div>
  <div class="rule" style="left:271px;top:1746px"></div>

  <div class="svc-name" style="left:468px;top:1686px;width:262px">Procurement of<br>Furniture</div>
  <div class="svc-sub" style="left:468px;top:1731px;width:262px">Accents, Art, Fixtures and<br>Fittings</div>
  <div class="rule" style="left:564px;top:1790px"></div>

  <div class="svc-name" style="left:762px;top:1686px;width:263px">Selection of Paints</div>
  <div class="svc-sub" style="left:762px;top:1709px;width:263px">Finishes and Construction<br>Materials</div>
  <div class="rule" style="left:858px;top:1764px"></div>

  <div class="dot" style="left:572px;top:1852px;background:var(--dark)"></div>
  <div class="dot" style="left:604px;top:1852px;background:var(--line)"></div>
</section>

<section>
  <svg class="abs" style="left:590px;top:1890px" width="190" height="140" viewBox="0 0 190 140">
    <polygon points="102,3 182,83 102,163 22,83" fill="none" stroke="#e2e2e2" stroke-width="1.5"/>
  </svg>
  <h2 class="abs sec-title" style="top:1935px">OUR <b>GALLERY</b></h2>

  <div class="photo" style="left:177px;top:2026px;width:412px;height:398px;background:linear-gradient(180deg,var(--tone-1),var(--tone-2) 70%,var(--tone-4))" role="img" aria-label="White kitchen with range hood and marble counters"></div>
  <div class="abs caption"><strong>Architectural</strong><span>Clara Beth Holloway has extensive design.</span></div>
  <div class="photo" style="left:609px;top:2026px;width:201px;height:196px;background:linear-gradient(180deg,#f2f2f2,var(--tone-2))" role="img" aria-label="White spiral staircase"></div>
  <div class="photo" style="left:823px;top:2026px;width:202px;height:196px;background:linear-gradient(180deg,var(--tone-4),var(--tone-6))" role="img" aria-label="Library corner with bookshelves and armchair"></div>
  <div class="photo" style="left:609px;top:2235px;width:416px;height:189px;background:linear-gradient(180deg,var(--tone-3),var(--tone-1))" role="img" aria-label="Lounge with curved sofa and flowers"></div>
  <div class="photo" style="left:177px;top:2440px;width:198px;height:196px;background:linear-gradient(180deg,var(--tone-2),var(--tone-5))" role="img" aria-label="Staircase with dark treads"></div>
  <div class="photo" style="left:390px;top:2440px;width:201px;height:196px;background:linear-gradient(180deg,var(--tone-3),var(--tone-1) 60%,var(--tone-5))" role="img" aria-label="Dining room with white chairs"></div>
  <div class="photo" style="left:177px;top:2651px;width:414px;height:187px;background:linear-gradient(180deg,var(--tone-4),var(--tone-3))" role="img" aria-label="Den with fireplace, bookshelves and armchairs"></div>
  <div class="photo" style="left:611px;top:2440px;width:414px;height:398px;background:linear-gradient(180deg,var(--tone-2),var(--tone-4) 55%,var(--tone-3))" role="img" aria-label="Covered patio with seating in front of tall windows"></div>

  <a class="btn gallery-btn">View All Projects</a>
</section>

<section>
  <div class="abs contact-band"></div>
  <h2 class="abs sec-title" style="top:3073px">CONTACT <b>US</b></h2>
  <p class="abs contact-lead">Lorem Ipsum is simply dummy text of the printing and typesetting industry. Lorem Ipsum has been the industry's standard dummy text ever since the 1500s</p>
  <div class="abs form-card"></div>
  <div class="field" style="left:222px;top:3263px;width:369px;height:56px">Name</div>
  <div class="field" style="left:609px;top:3263px;width:369px;height:56px">Phone</div>
  <div class="field" style="left:222px;top:3354px;width:369px;height:56px">Email</div>
  <div class="field" style="left:609px;top:3354px;width:369px;height:56px">Subject</div>
  <div class="field" style="left:222px;top:3445px;width:756px;height:140px">Message</div>
  <a class="btn send-btn">Send Message</a>
  <div class="abs contact-line" style="left:227px">Phone : 000 999 0000</div>
  <div class="abs contact-line" style="left:534px">Email: clarabeth@info.example</div>
</section>

<footer>
  <div class="abs foot-name">CLARA BETH HOLLOWAY</div>
  <div class="abs foot-sub">INTERIORS</div>
  <span class="foot-link" style="left:330px">HOME</span>
  <span class="foot-link" style="left:461px">ABOUT</span>
  <span class="foot-link" style="left:592px">SERVICES</span>
  <span class="foot-link" style="left:724px">GALLERY</span>
  <span class="foot-link" style="left:853px">CONTACT</span>
  <svg class="abs" style="left:554px;top:4143px" width="90" height="22" viewBox="0 0 90 22">
    <circle cx="11" cy="11" r="8" fill="none" stroke="#9a9a9a" stroke-width="2"/>
    <circle cx="43" cy="11" r="8" fill="none" stroke="#9a9a9a" stroke-width="2"/>
    <circle cx="75" cy="11" r="8" fill="none" stroke="#9a9a9a" stroke-width="2"/>
  </svg>
  <div class="abs foot-rule"></div>
  <p class="abs copy">© Clara Beth Holloway interiors 2020 All rights reserved.</p>
</footer>

</body>
</html>
```